Design for web app with Plinkora Stratum Craft - Tarvo7 SMS consult

We are developing a web app that will work in browsers. Its main purpose is to allow for users (signing up and logging in with their phone number) to track their habbits and select consultants to whom they can send SMS for help.

The wireframes of the app can be accessed here (pdf):
https://files.plinkora.example/d/7K2mWqLzXv4NtRb9HcJpYsAeUfDg3/view

NB!: Please do not follow the mockups 100% literally, but the Plinkora Stratum craft guidelines.

The technical specifications and descriptions of the web app's functionalities are available in the link below:
https://papers.plinkora.example/doc/4HsTnV8bQeZr2LmXwYcKpDjAuFgN6oRiE5tW1yMx/edit

Requirements for the design:

- The design should be provided as PSD, where each page/section should be in its own PSD file OR all pages/sections should be represented as folder groups in a single PSD file.

- All graphical elements in the design should be delivered as single layers which can then be extracted from the PSD.

- All graphical elements (icons, graphical buttons, etc.) should be provided as vector objects in the PSD, so that they can be exported into different sizes without loss of quality (for responsiveness).

- The design should use either web safe fonts or Plinkora Type.

Instructions for the design:
The design should be based on Plinkora Stratum Craft - http://www.plinkora.example/craft/spec/stratum-craft/overview.html

Please also provide an app icon and suggest a logo for the app.

Requirements
Must have
• Based on Plinkora Stratum Craft
• Flat
Nice to have
• Nice looking and not so stiff as the default Plinkora Stratum Craft, but it is important to follow their guidelines.
Should not have
• 3D

```html
<!DOCTYPE html>
<html lang="en">
<head>
<meta charset="utf-8">
<title>Tarvo7 – SMS consult web app</title>
<link href="https://fonts.googleapis.com/css2?family=Titillium+Web:wght@300;400;600&family=Open+Sans:wght@400;600&display=swap" rel="stylesheet">
<style>
  :root {
    --header-dark: #3a3e49;
    --header-dark-2: #2f323b;
    --stage-light: #9a9a9a;
    --stage-mid: #7a7a7a;
    --stage-dark: #555759;
    --screen-dark: #3f4452;
    --screen-darker: #363a46;
    --bar-dark: #3b404c;
    --primary-blue: #1e74b6;
    --sky-blue: #3cb5e8;
    --accent-yellow: #f7c34a;
    --accent-green: #2fc17a;
    --accent-red: #f0604a;
    --row-light: #f1f1f1;
    --row-white: #ffffff;
    --text-dark: #3a3d44;
    --text-soft: #7b7f88;
    --text-light: #ffffff;
    --icon-ink: #2f3340;
    --footer-grey: #e6e6e6;
    --footer-orange: #ef5b3b;
    --section-grey: #5b5e66;
  }
  * { box-sizing: border-box; margin: 0; padding: 0; }
  html, body { width: 993px; height: 1200px; overflow: hidden; }
  body {
    position: relative;
    font-family: "Titillium Web", "Open Sans", sans-serif;
    background: #ffffff;
  }

  /* Header band */
  .site-header {
    position: absolute; left: 0; top: 0; width: 993px; height: 144px;
    background: linear-gradient(180deg, var(--header-dark) 0%, var(--header-dark-2) 100%);
  }
  .brand {
    position: absolute; left: 36px; top: 44px;
    display: flex; align-items: center; gap: 10px;
  }
  .brand-square { width: 22px; height: 22px; background: var(--primary-blue); }
  .brand-name {
    font-family: "Titillium Web", sans-serif; font-weight: 600;
    font-size: 30px; color: var(--text-light); letter-spacing: 1px; line-height: 1;
  }

  /* Stage with app screens */
  .stage {
    position: absolute; left: 0; top: 144px; width: 993px; height: 679px;
    background: radial-gradient(ellipse at 50% 40%, var(--stage-light) 0%, var(--stage-mid) 45%, var(--stage-dark) 100%);
  }
  .screen {
    position: absolute; overflow: hidden;
    box-shadow: 0 6px 18px rgba(0,0,0,.35);
  }

  /* List screen */
  .screen-list { left: 67px; top: 87px; width: 253px; height: 405px; background: var(--row-white); }
  .app-bar {
    height: 52px; background: var(--bar-dark); color: var(--text-light);
    display: flex; align-items: center; gap: 14px; padding: 0 16px;
    font-family: "Open Sans", sans-serif; font-size: 13px;
  }
  .list-row {
    height: 45px; display: flex; align-items: center; padding-left: 18px;
    font-family: "Open Sans", sans-serif; font-size: 11.5px; color: var(--text-dark);
  }
  .list-row:nth-child(even) { background: var(--row-light); }
  .list-action {
    position: absolute; left: 10px; right: 10px; bottom: 8px; height: 36px;
    background: var(--primary-blue); color: var(--text-light);
    font-family: "Open Sans", sans-serif; font-size: 12px;
    display: flex; align-items: center; justify-content: center;
  }

  /* Form screens */
  .screen-form { width: 253px; height: 440px; top: 69px; background: var(--screen-dark); }
  .screen-signin { left: 171px; }
  .screen-register { left: 570px; }
  .form-title {
    position: absolute; left: 0; right: 0; text-align: center;
    color: var(--text-light); font-weight: 400; font-size: 19px; letter-spacing: 1px;
  }
  .field {
    position: absolute; left: 19px; right: 19px; height: 36px; background: var(--row-white);
    display: flex; align-items: center; padding-left: 12px;
  }
  .button {
    position: absolute; left: 19px; right: 19px; height: 38px;
    display: flex; align-items: center; justify-content: center;
    font-family: "Open Sans", sans-serif; font-size: 11px; letter-spacing: .5px;
    box-shadow: 0 2px 3px rgba(0,0,0,.3);
  }
  .button-primary { background: var(--primary-blue); color: var(--text-light); }
  .button-secondary { background: var(--accent-yellow); color: var(--text-dark); }
  .form-link {
    position: absolute; left: 0; right: 0; text-align: center;
    font-family: "Open Sans", sans-serif; font-size: 9px; color: #d5d8de; letter-spacing: .4px;
  }

  /* Notes screen */
  .screen-notes { left: 674px; top: 87px; width: 253px; height: 405px; background: #eeeff1; }
  .notes-date {
    height: 36px; background: var(--sky-blue); color: var(--text-light);
    display: flex; align-items: center; justify-content: space-between; padding: 0 14px 0 18px;
    font-family: "Open Sans", sans-serif; font-size: 12px;
  }
  .vote-row { display: flex; margin: 12px 10px 0; height: 46px; }
  .vote { flex: 1; display: flex; align-items: center; justify-content: center; }
  .vote-up { background: var(--accent-green); }
  .vote-down { background: var(--accent-red); }
  .notes-field {
    margin: 8px 10px 0; height: 30px; background: var(--row-white);
    font-family: "Open Sans", sans-serif; font-size: 9px; color: var(--text-soft);
    display: flex; align-items: center; padding-left: 10px;
  }
  .notes-area { margin: 32px 10px 0; height: 134px; background: var(--row-white); }
  .notes-save {
    position: absolute; left: 10px; right: 10px; bottom: 9px; height: 34px;
    background: var(--accent-yellow); color: var(--text-dark);
    font-family: "Open Sans", sans-serif; font-size: 11px;
    display: flex; align-items: center; justify-content: center;
  }

  /* Splash screen */
  .screen-splash {
    left: 336px; top: 47px; width: 275px; height: 486px;
    background: linear-gradient(115deg, var(--screen-darker) 0%, var(--screen-dark) 48%, #4b505e 49%, var(--screen-dark) 100%);
    box-shadow: 0 10px 28px rgba(0,0,0,.45);
  }
  .splash-brand {
    position: absolute; left: 0; right: 0; top: 222px;
    display: flex; align-items: center; justify-content: center; gap: 10px;
  }
  .splash-brand .brand-square { width: 20px; height: 20px; }
  .splash-brand .brand-name { font-size: 27px; }
  .splash-legal {
    position: absolute; left: 20px; right: 20px; bottom: 18px; text-align: center;
    font-family: "Open Sans", sans-serif; color: #9ea3ad; font-size: 6.5px; line-height: 1.45;
  }
  .splash-legal .copyright { font-size: 7.5px; margin-bottom: 8px; display: block; }

  /* Icon showcase */
  .icon-section {
    position: absolute; left: 0; top: 823px; width: 993px; height: 248px; background: #ffffff;
  }
  .section-title {
    position: absolute; left: 0; right: 0; top: 48px; text-align: center;
    font-weight: 300; font-size: 24px; color: var(--section-grey);
  }
  .icon-row { position: absolute; left: 0; top: 126px; width: 993px; height: 60px; }
  .icon-row svg { position: absolute; top: 0; }

  /* Footer band */
  .site-footer {
    position: absolute; left: 0; top: 1071px; width: 993px; height: 129px;
    background: var(--footer-grey); border-top: 1px solid #d4d4d4;
    display: flex; align-items: center; justify-content: center;
  }
  .footer-note { color: var(--footer-orange); font-weight: 400; font-size: 24px; letter-spacing: .5px; }
</style>
</head>
<body>

<header class="site-header">
  <div class="brand">
    <span class="brand-square"></span>
    <span class="brand-name">Tarvo7</span>
  </div>
</header>

<section class="stage" aria-label="App screens">

  <!-- Consultant list -->
  <div class="screen screen-list">
    <div class="app-bar">
      <svg width="16" height="14" viewBox="0 0 16 14"><path d="M15 7H2M7 1L1 7l6 6" fill="none" stroke="#fff" stroke-width="1.8"/></svg>
      <span>Select your consultant</span>
    </div>
    <div class="list-rows">
      <div class="list-row">Lorem Ipsum</div>
      <div class="list-row">Dolor sit amet</div>
      <div class="list-row">Consectetuer</div>
      <div class="list-row">Adipiscing</div>
      <div class="list-row">Nonummy</div>
      <div class="list-row">Euismod</div>
      <div class="list-row">Tincidunt</div>
    </div>
    <div class="list-action">Continue</div>
  </div>

  <!-- Sign in -->
  <div class="screen screen-form screen-signin">
    <div class="form-title" style="top:101px">SIGN IN</div>
    <div class="field" style="top:138px">
      <svg width="10" height="16" viewBox="0 0 10 16"><rect x="1" y="1" width="8" height="14" rx="1.5" fill="none" stroke="#9aa0aa" stroke-width="1.4"/></svg>
    </div>
    <div class="field" style="top:182px">
      <svg width="10" height="12" viewBox="0 0 10 12"><rect x="1" y="5" width="8" height="6.5" fill="#9aa0aa"/><path d="M2.8 5V3.4a2.2 2.2 0 0 1 4.4 0V5" fill="none" stroke="#9aa0aa" stroke-width="1.3"/></svg>
    </div>
    <div class="button button-primary" style="top:224px">LOGIN</div>
    <div class="button button-secondary" style="top:272px">REGISTER</div>
    <div class="form-link" style="top:330px">FORGOT PASSWORD?</div>
  </div>

  <!-- Register -->
  <div class="screen screen-form screen-register">
    <div class="form-title" style="top:136px">REGISTER</div>
    <div class="field" style="top:173px"></div>
    <div class="button button-primary" style="top:216px">LOGIN</div>
    <div class="button button-secondary" style="top:261px">CANCEL</div>
  </div>

  <!-- Notes -->
  <div class="screen screen-notes">
    <div class="app-bar">
      <svg width="16" height="14" viewBox="0 0 16 14"><path d="M15 7H2M7 1L1 7l6 6" fill="none" stroke="#fff" stroke-width="1.8"/></svg>
      <span>Notes</span>
    </div>
    <div class="notes-date">
      <span>12.05.2015</span>
      <svg width="8" height="13" viewBox="0 0 8 13"><path d="M1 1l5.5 5.5L1 12" fill="none" stroke="#fff" stroke-width="1.8"/></svg>
    </div>
    <div class="vote-row">
      <div class="vote vote-up">
        <svg width="20" height="20" viewBox="0 0 40 40"><path d="M4 18h7v18H4zM11 19l8-14c3 0 4 2 3.5 5L21 16h11a3 3 0 0 1 3 3.5L33 32a4 4 0 0 1-4 4H11" fill="none" stroke="#fff" stroke-width="3" stroke-linejoin="round"/></svg>
      </div>
      <div class="vote vote-down">
        <svg width="20" height="20" viewBox="0 0 40 40"><g transform="rotate(180 20 20)"><path d="M4 18h7v18H4zM11 19l8-14c3 0 4 2 3.5 5L21 16h11a3 3 0 0 1 3 3.5L33 32a4 4 0 0 1-4 4H11" fill="none" stroke="#fff" stroke-width="3" stroke-linejoin="round"/></g></svg>
      </div>
    </div>
    <div class="notes-field">Evaluation</div>
    <div class="notes-area"></div>
    <div class="notes-save">Gem</div>
  </div>

  <!-- Splash -->
  <div class="screen screen-splash">
    <div class="splash-brand">
      <span class="brand-square"></span>
      <span class="brand-name">Tarvo7</span>
    </div>
    <p class="splash-legal">
      <span class="copyright">(C) 2015, COMPANY HERE</span>
      Track habits daily and reach a trusted consultant by SMS whenever you need a hand.
    </p>
  </div>
</section>

<section class="icon-section">
  <h2 class="section-title">ICONS ( Vector Based )</h2>
  <div class="icon-row">
    <!-- phone -->
    <svg style="left:124px" width="60" height="60" viewBox="0 0 60 60"><path d="M14 6l9 11-5 6c3 7 9 13 16 17l6-5 11 9-7 9C26 52 8 34 5 13z" fill="none" stroke="var(--icon-ink)" stroke-width="3.2" stroke-linejoin="round"/></svg>
    <!-- thumbs up -->
    <svg style="left:221px" width="60" height="60" viewBox="0 0 40 40"><path d="M4 18h7v18H4zM11 19l8-14c3 0 4 2 3.5 5L21 16h11a3 3 0 0 1 3 3.5L33 32a4 4 0 0 1-4 4H11" fill="none" stroke="var(--icon-ink)" stroke-width="2.2" stroke-linejoin="round"/></svg>
    <!-- thumbs down -->
    <svg style="left:319px" width="60" height="60" viewBox="0 0 40 40"><g transform="rotate(180 20 20)"><path d="M4 18h7v18H4zM11 19l8-14c3 0 4 2 3.5 5L21 16h11a3 3 0 0 1 3 3.5L33 32a4 4 0 0 1-4 4H11" fill="none" stroke="var(--icon-ink)" stroke-width="2.2" stroke-linejoin="round"/></g></svg>
    <!-- chevron -->
    <svg style="left:405px" width="30" height="60" viewBox="0 0 30 60"><path d="M8 18l13 12-13 12" fill="none" stroke="var(--icon-ink)" stroke-width="3"/></svg>
    <!-- chart -->
    <svg style="left:478px" width="60" height="60" viewBox="0 0 60 60"><path d="M6 6v48h50" fill="none" stroke="var(--icon-ink)" stroke-width="4"/><path d="M13 44l11-13 8 7 15-16" fill="none" stroke="var(--icon-ink)" stroke-width="4"/><path d="M40 20h10v10z" fill="var(--icon-ink)"/></svg>
    <!-- tick -->
    <svg style="left:567px" width="52" height="60" viewBox="0 0 52 60"><path d="M3 32l14 13L49 15" fill="none" stroke="var(--icon-ink)" stroke-width="3"/></svg>
    <!-- chat -->
    <svg style="left:646px" width="54" height="60" viewBox="0 0 54 60"><path d="M6 14h42a3 3 0 0 1 3 3v21a3 3 0 0 1-3 3H20l-9 8v-8H6a3 3 0 0 1-3-3V17a3 3 0 0 1 3-3z" fill="var(--icon-ink)"/></svg>
    <!-- mobile -->
    <svg style="left:750px" width="36" height="60" viewBox="0 0 36 60"><rect x="5" y="3" width="26" height="54" rx="3" fill="none" stroke="var(--icon-ink)" stroke-width="3"/><rect x="14" y="49" width="8" height="2.5" fill="var(--icon-ink)"/></svg>
    <!-- unlocked padlock -->
    <svg style="left:831px" width="40" height="60" viewBox="0 0 40 60"><path d="M11 26V15a9 9 0 0 1 18 0v3" fill="none" stroke="var(--icon-ink)" stroke-width="4"/><rect x="4" y="26" width="32" height="28" fill="var(--icon-ink)"/><circle cx="20" cy="37" r="3.5" fill="#fff"/><rect x="18.5" y="38" width="3" height="9" fill="#fff"/></svg>
  </div>
</section>

<footer class="site-footer">
  <p class="footer-note">FOLLOW THE LINKS FOR DETAILS</p>
</footer>

</body>
</html>
```